Detail Shop Business card design

i need a business card design for my new detailing company called 'Brenner's Detail Shop'. i want an all black and white design . simple, direct and to the point. i want the designer to choose a fitting font to match the logothe front should have logo, address, phone and email and the back side should have a slogan and text indicating that we offer services on anything including cars, trucks, motorcycles and RVs. slogan will read "we take pride in your ride"
maybe also very small on the back side the IG icon with Brenners_Detail_Shop

phone 482.615.7734
address 7384 E Harlow Ave
Spokane WA 99342
email: BrennersDetail@quorvail.com

Target Market(s)

all ages , auto enthusiasts

Industry/Entity Type

Automotive

Contact Information for Business Card

the front should have logo, address, phone and email and the back side should have a slogan and text indicating that we offer services on anything including cars, trucks, motorcycles and RVs. slogan will read "we take pride in your ride"

phone 482.615.7734
address 7384 E Harlow Ave
Spokane WA 99342

Colors
000000
ffffff

Requirements
Must have
• bold font and very simple design with good spacing
Nice to have
• anything creative from the designer indicating we service any types of vehicles
Should not have
• any colors ,

```html
<!DOCTYPE html>
<html lang="en">
<head>
<meta charset="utf-8">
<title>Brenner's Detail Shop – Business Cards</title>
<link href="https://fonts.googleapis.com/css2?family=Roboto+Slab:wght@400;700&display=swap" rel="stylesheet">
<style>
  :root {
    --ink: #000000;
    --paper: #ffffff;
    --stage: #2b2b2b;
    --soft-ink: #1a1a1a;
    --muted: #444444;
    --card-w: 600px;
    --card-h: 343px;
  }
  * { box-sizing: border-box; margin: 0; padding: 0; }
  html, body {
    width: 1200px; height: 930px; overflow: hidden;
    background: var(--stage);
    font-family: "Roboto Slab", Georgia, serif;
  }
  .stage { position: relative; width: 1200px; height: 930px; }
  .card {
    position: absolute; left: 300px;
    width: var(--card-w); height: var(--card-h);
    border-radius: 16px; overflow: hidden;
  }
  /* back side */
  .card--back { top: 90px; background: var(--ink); color: var(--paper); }
  .card--back .brand {
    position: absolute; top: 40px; left: 0; right: 0;
    display: flex; flex-direction: column; align-items: center; gap: 12px;
  }
  .vehicle-art {
    width: 150px; height: 80px; border-radius: 75px 75px 8px 8px;
    background: linear-gradient(180deg, #e6e6e6, #9a9a9a);
  }
  .brand-name {
    font-weight: 700; font-size: 20px; letter-spacing: 1px; text-transform: uppercase;
    display: flex; align-items: center; gap: 8px;
  }
  .brand-dot { width: 10px; height: 10px; border-radius: 50%; background: currentColor; }
  .slogan {
    position: absolute; top: 220px; left: 0; right: 0;
    display: flex; align-items: center; justify-content: center; gap: 14px;
    font-size: 15px; letter-spacing: 1.5px; text-transform: uppercase;
  }
  .slogan .rule { width: 70px; height: 1px; background: var(--paper); }
  .services {
    position: absolute; top: 258px; left: 0; right: 0; text-align: center;
    font-size: 17px; letter-spacing: 1.5px; text-transform: uppercase;
  }
  /* front side */
  .card--front { top: 497px; background: var(--paper); color: var(--soft-ink); }
  .person { position: absolute; left: 40px; top: 78px; }
  .person-name { font-weight: 700; font-size: 24px; text-transform: uppercase; letter-spacing: 0.5px; color: var(--ink); }
  .person-role { font-size: 14px; color: var(--muted); margin-top: 2px; }
  .address { position: absolute; left: 96px; top: 170px; font-size: 15px; line-height: 1.3; }
  .contacts { position: absolute; left: 96px; top: 250px; list-style: none; font-size: 15px; line-height: 1.35; }
  .contacts li { display: flex; align-items: center; gap: 8px; }
  .contacts svg { width: 12px; height: 12px; flex: none; }
  .card--front .brand {
    position: absolute; right: 40px; top: 40px; width: 230px;
    display: flex; flex-direction: column; align-items: center; gap: 14px;
  }
  .card--front .vehicle-art { width: 220px; height: 150px; border-radius: 110px 110px 10px 10px;
    background: linear-gradient(180deg, #3a3a3a, #0d0d0d); }
  .card--front .brand-name { color: var(--ink); font-size: 20px; }
</style>
</head>
<body>
<main class="stage">
  <section class="card card--back" aria-label="Card back">
    <div class="brand">
      <div class="vehicle-art" role="img" aria-label="Hot rod illustration in a round emblem"></div>
      <div class="brand-name"><span class="brand-dot"></span>Brenner's Detail Shop</div>
    </div>
    <p class="slogan"><span class="rule"></span>We take pride in your ride<span class="rule"></span></p>
    <p class="services">Cars - Trucks - Motorcycles and RVs</p>
  </section>

  <section class="card card--front" aria-label="Card front">
    <div class="person">
      <h1 class="person-name">Declan Marsh</h1>
      <p class="person-role">Director</p>
    </div>
    <address class="address">7384 E Harlow Ave<br>Spokane WA 99342</address>
    <ul class="contacts">
      <li><svg viewBox="0 0 12 12"><path d="M2 1h2.5l1 2.5-1.3 1a6 6 0 0 0 3.3 3.3l1-1.3L11 7.5V10a1 1 0 0 1-1 1A9 9 0 0 1 1 2a1 1 0 0 1 1-1z" fill="#000"/></svg>482.615.7734</li>
      <li><svg viewBox="0 0 12 12"><rect x="0.75" y="2.25" width="10.5" height="7.5" fill="none" stroke="#000" stroke-width="1.2"/><path d="M1 2.5 6 6.5 11 2.5" fill="none" stroke="#000" stroke-width="1.2"/></svg>BrennersDetail@quorvail.com</li>
      <li><svg viewBox="0 0 12 12"><circle cx="6" cy="6" r="5.2" fill="none" stroke="#000" stroke-width="1.1"/><path d="M0.8 6h10.4M6 0.8c-2.5 3-2.5 7.4 0 10.4M6 0.8c2.5 3 2.5 7.4 0 10.4" fill="none" stroke="#000" stroke-width="0.9"/></svg>www.BrennersDetail.com</li>
    </ul>
    <div class="brand">
      <div class="vehicle-art" role="img" aria-label="Hot rod illustration in a round emblem"></div>
      <div class="brand-name"><span class="brand-dot"></span>Brenner's Detail Shop</div>
    </div>
  </section>
</main>
</body>
</html>
```